Team email banner for internal communications

We need a team email banner/header that will be applied to all internal communications from our department to other functions. The graphic should be optimized for Outlook and be landscape in layout. We have 5 different silo within our team and will need so will either need have a blank space to denote each team or have change in colors/graphics to denote each team (see current headers attached to job description). We are looking for a banner that combines our team logo (attached) with our team name, Commercial Learning & Development. The theme should be L&D and pharmaceutical in nature.

Need extra days to review

The text in the banner should be Commercial Learning & Development with the team logo (attached).

```html
<!DOCTYPE html>
<html lang="en">
<head>
<meta charset="utf-8">
<title>Commercial Learning &amp; Development – Team Email Banners</title>
<link rel="stylesheet" href="https://fonts.googleapis.com/css2?family=Montserrat:wght@400;500;700;800&display=swap">
<style>
  :root {
    --backdrop: #58585a;
    --paper: #ffffff;
    --ink: #050608;
    --muted: #a7a7a9;
    --market-blue: #1b8acb;
    --ops-navy: #0b4f7c;
    --leader-red: #e02826;
    --heme-red: #b5232e;
    --tumor-purple: #5e2570;
    --logo-red: #e02826;
  }
  * { box-sizing: border-box; margin: 0; padding: 0; }
  html, body {
    width: 1200px; height: 784px; overflow: hidden;
    background: var(--backdrop);
    font-family: "Montserrat", Arial, sans-serif;
  }
  .board { position: relative; width: 1200px; height: 784px; }

  .banner {
    position: absolute; width: 466px; height: 155px;
    background: var(--paper); overflow: hidden;
  }
  .banner--overview   { left: 97px;  top: 107px; --accent: var(--leader-red); }
  .banner--market     { left: 637px; top: 107px; --accent: var(--market-blue); }
  .banner--leadership { left: 97px;  top: 314px; --accent: var(--leader-red); }
  .banner--operations { left: 637px; top: 314px; --accent: var(--ops-navy); }
  .banner--hematology { left: 97px;  top: 521px; --accent: var(--heme-red); }
  .banner--tumor      { left: 637px; top: 518px; --accent: var(--tumor-purple); }

  .banner__frame { position: absolute; inset: 0; width: 466px; height: 155px; }
  .banner__wedge { fill: var(--accent); }
  .banner__topbar { fill: var(--ink); }

  .team-logo {
    position: absolute; left: 58px; top: 64px;
    display: flex; align-items: center; gap: 6px;
    font-weight: 700; font-size: 17px; color: var(--logo-red);
  }
  .team-logo__dot {
    width: 14px; height: 14px; border-radius: 50%; background: var(--logo-red);
  }

  .title {
    position: absolute; left: 161px; top: 47px;
    font-weight: 800; font-size: 38px; line-height: 1;
    letter-spacing: 2.6px; color: var(--ink);
  }
  .subtitle {
    position: absolute; left: 162px; top: 88px;
    font-weight: 500; font-size: 14.6px; line-height: 1;
    letter-spacing: 0.7px; color: var(--ink);
  }
  .team-stripe {
    position: absolute; left: 161px; right: 0; top: 111px; height: 6px;
    display: flex;
  }
  .team-stripe span { flex: 1; background: var(--muted); }
  .team-stripe .is-market     { --c: var(--market-blue); }
  .team-stripe .is-operations { --c: var(--ops-navy); }
  .team-stripe .is-leadership { --c: var(--leader-red); }
  .team-stripe .is-hematology { --c: var(--heme-red); }
  .team-stripe .is-tumor      { --c: var(--tumor-purple); }
  .team-stripe--all span,
  .team-stripe span.is-active { background: var(--c); }

  .team-name {
    position: absolute; left: 162px; top: 125px;
    font-weight: 400; font-size: 15px; line-height: 1;
    letter-spacing: 1px; color: var(--accent);
  }
</style>
</head>
<body>
<main class="board">

  <section class="banner banner--overview">
    <svg class="banner__frame" viewBox="0 0 466 155" aria-hidden="true">
      <polygon class="banner__wedge" points="0,0 47,0 0,111"/>
      <polygon class="banner__topbar" points="262,0 466,0 466,15 274,15"/>
    </svg>
    <div class="team-logo"><span class="team-logo__dot"></span>Kestrel</div>
    <h1 class="title">COMMERCIAL</h1>
    <p class="subtitle">LEARNING &amp; DEVELOPMENT</p>
    <div class="team-stripe team-stripe--all">
      <span class="is-market"></span><span class="is-operations"></span><span class="is-leadership"></span><span class="is-hematology"></span><span class="is-tumor"></span>
    </div>
  </section>

  <section class="banner banner--market">
    <svg class="banner__frame" viewBox="0 0 466 155" aria-hidden="true">
      <polygon class="banner__wedge" points="0,0 47,0 0,111"/>
      <polygon class="banner__topbar" points="262,0 466,0 466,15 274,15"/>
    </svg>
    <div class="team-logo"><span class="team-logo__dot"></span>Kestrel</div>
    <h1 class="title">COMMERCIAL</h1>
    <p class="subtitle">LEARNING &amp; DEVELOPMENT</p>
    <div class="team-stripe">
      <span class="is-market is-active"></span><span></span><span></span><span></span><span></span>
    </div>
    <p class="team-name">MARKET ACCESS</p>
  </section>

  <section class="banner banner--leadership">
    <svg class="banner__frame" viewBox="0 0 466 155" aria-hidden="true">
      <polygon class="banner__wedge" points="0,0 47,0 0,111"/>
      <polygon class="banner__topbar" points="262,0 466,0 466,15 274,15"/>
    </svg>
    <div class="team-logo"><span class="team-logo__dot"></span>Kestrel</div>
    <h1 class="title">COMMERCIAL</h1>
    <p class="subtitle">LEARNING &amp; DEVELOPMENT</p>
    <div class="team-stripe">
      <span></span><span></span><span class="is-leadership is-active"></span><span></span><span></span>
    </div>
    <p class="team-name">LEADERSHIP DEVELOPMENT</p>
  </section>

  <section class="banner banner--operations">
    <svg class="banner__frame" viewBox="0 0 466 155" aria-hidden="true">
      <polygon class="banner__wedge" points="0,0 47,0 0,111"/>
      <polygon class="banner__topbar" points="262,0 466,0 466,15 274,15"/>
    </svg>
    <div class="team-logo"><span class="team-logo__dot"></span>Kestrel</div>
    <h1 class="title">COMMERCIAL</h1>
    <p class="subtitle">LEARNING &amp; DEVELOPMENT</p>
    <div class="team-stripe">
      <span></span><span class="is-operations is-active"></span><span></span><span></span><span></span>
    </div>
    <p class="team-name">OPERATIONS &amp; CAPABILITES</p>
  </section>

  <section class="banner banner--hematology">
    <svg class="banner__frame" viewBox="0 0 466 155" aria-hidden="true">
      <polygon class="banner__wedge" points="0,0 47,0 0,111"/>
      <polygon class="banner__topbar" points="262,0 466,0 466,15 274,15"/>
    </svg>
    <div class="team-logo"><span class="team-logo__dot"></span>Kestrel</div>
    <h1 class="title">COMMERCIAL</h1>
    <p class="subtitle">LEARNING &amp; DEVELOPMENT</p>
    <div class="team-stripe">
      <span></span><span></span><span></span><span class="is-hematology is-active"></span><span></span>
    </div>
    <p class="team-name">HEMATOLOGY</p>
  </section>

  <section class="banner banner--tumor">
    <svg class="banner__frame" viewBox="0 0 466 155" aria-hidden="true">
      <polygon class="banner__wedge" points="0,0 47,0 0,111"/>
      <polygon class="banner__topbar" points="262,0 466,0 466,15 274,15"/>
    </svg>
    <div class="team-logo"><span class="team-logo__dot"></span>Kestrel</div>
    <h1 class="title">COMMERCIAL</h1>
    <p class="subtitle">LEARNING &amp; DEVELOPMENT</p>
    <div class="team-stripe">
      <span></span><span></span><span></span><span></span><span class="is-tumor is-active"></span>
    </div>
    <p class="team-name">SOLID TUMOR</p>
  </section>

</main>
</body>
</html>
```